Church Bulletin Ad (see attached sample)

Create a New Church Bulletin Ad. I have attached some samples of what we would like to have in the ad. (1) Marrowfield Realty Thorne Logo (2) Headshot (3) Lena Vasko & Greta Vasko, Real Estate Team (4) Phone number (5) Email address (6) St Aldwin Parishioners for over 40 Years. We would like for the ad to be clean and modern. NO OTHER IMAGES besides headshots and Marrowfield Realty Thorne Logo.

Target Market(s)

Church community

Industry/Entity Type

Real Estate

Font styles to use
Sans Serif
Other font styles liked:
• Modern Font

Colors
0054AA
0677BA
7BADD7
CADEEF
E8F1F8

Requirements
Must have
• Marrowfield Realty Thorne Logo; Headshot; Ad size is 4.5"x1.62"

```html
<!DOCTYPE html>
<html lang="en">
<head>
<meta charset="UTF-8">
<title>St Aldwin Bulletin Ad – Lena &amp; Greta Vasko</title>
<link rel="stylesheet" href="https://fonts.googleapis.com/css2?family=Montserrat:ital,wght@0,400;0,600;0,800;1,400;1,800&display=swap">
<style>
  :root {
    --navy: #0c2b53;
    --band: #12578c;
    --accent: #1b9be0;
    --white: #ffffff;
    --page: #ffffff;
    --photo-light: #e9eef3;
    --photo-dark: #2a2a2e;
  }
  * { box-sizing: border-box; margin: 0; padding: 0; }
  html, body {
    width: 1200px; height: 1200px; overflow: hidden;
    background: var(--page);
    font-family: "Montserrat", Arial, sans-serif;
  }
  .ad {
    position: absolute; left: 133px; top: 434px;
    width: 941px; height: 339px;
    background: var(--navy);
    box-shadow: -2px 3px 6px rgba(0,0,0,0.35);
    color: var(--white);
  }
  .brand-mark {
    position: absolute; left: 109px; top: 41px;
    width: 160px; height: 145px;
    border: 3px solid var(--white);
    display: flex; align-items: center; justify-content: center;
    text-align: center; padding: 12px;
  }
  .brand-name {
    font-weight: 600; font-size: 19px; line-height: 1.25;
    color: var(--white); letter-spacing: 0.5px;
  }
  .team {
    position: absolute; left: 0; top: 228px; width: 378px;
    text-align: center;
  }
  .team-names {
    font-weight: 800; font-style: italic; font-size: 21px;
    margin-left: 50px; white-space: nowrap;
  }
  .team-role {
    font-weight: 400; font-style: italic; font-size: 16px;
    margin-top: 2px; letter-spacing: 0.5px;
  }
  .headshot {
    position: absolute; top: 24px;
    width: 221px; height: 205px;
    border: 5px solid var(--white);
    box-shadow: 0 2px 5px rgba(0,0,0,0.4);
  }
  .headshot--lena {
    left: 426px;
    background: linear-gradient(180deg, var(--photo-light) 0%, #cdbcb0 45%, var(--photo-dark) 100%);
  }
  .headshot--greta {
    left: 664px;
    background: linear-gradient(180deg, #c9d2da 0%, #efe8e2 45%, var(--photo-dark) 100%);
  }
  .tagline {
    position: absolute; left: 426px; width: 459px; top: 250px;
    text-align: center; font-size: 17px; color: var(--accent);
    white-space: nowrap;
  }
  .tagline strong { font-weight: 800; font-style: italic; }
  .tagline em { font-weight: 400; font-style: italic; }
  .contact-band {
    position: absolute; left: 0; bottom: 0;
    width: 100%; height: 48px;
    background: var(--band);
    display: flex; align-items: center; justify-content: center; gap: 26px;
  }
  .contact-item {
    display: flex; align-items: center; gap: 9px;
    font-weight: 800; font-style: italic; font-size: 22px;
    padding-right: 12px;
  }
  .contact-icon { width: 32px; height: 32px; flex: none; }
</style>
</head>
<body>
  <div class="ad">
    <div class="brand-mark">
      <span class="brand-name">Marrowfield Realty Thorne</span>
    </div>

    <div class="team">
      <p class="team-names">Lena Vasko &amp; Greta Vasko,</p>
      <p class="team-role">Real Estate Team</p>
    </div>

    <div class="headshot headshot--lena" role="img" aria-label="Headshot of Lena Vasko"></div>
    <div class="headshot headshot--greta" role="img" aria-label="Headshot of Greta Vasko"></div>

    <p class="tagline"><strong>St Aldwin Parishioners</strong> <em>for over 40 Years.</em></p>

    <div class="contact-band">
      <div class="contact-item">
        <svg class="contact-icon" viewBox="0 0 32 32" aria-hidden="true">
          <circle cx="16" cy="16" r="14.5" fill="none" stroke="#fff" stroke-width="2"/>
          <path d="M11 8.5c.6-.4 1.3-.3 1.7.3l1.8 2.7c.4.6.3 1.3-.2 1.7l-1.2.9c.6 1.9 2.4 4 4.3 5l1-1.1c.5-.5 1.2-.5 1.7-.1l2.6 2c.5.4.6 1.2.2 1.7l-1.3 1.6c-.8 1-2.2 1.2-3.6.6-4.1-1.8-7.3-5.4-8.6-9.7-.4-1.4 0-2.7 1-3.3z" fill="#fff"/>
        </svg>
        <span>(206) 555-0148</span>
      </div>
      <div class="contact-item">
        <svg class="contact-icon" viewBox="0 0 32 32" aria-hidden="true">
          <circle cx="16" cy="16" r="14.5" fill="none" stroke="#fff" stroke-width="2"/>
          <rect x="9" y="11" width="14" height="10" rx="1.5" fill="#fff"/>
          <path d="M9.5 11.8 16 16.5l6.5-4.7" fill="none" stroke="#12578c" stroke-width="1.4"/>
        </svg>
        <span>vaskoteam@marrowthorne.com</span>
      </div>
    </div>
  </div>
</body>
</html>
```